Need A Modern Website Design For ADSL2+ Provider

AIM: To sell affordable combined ADSL2+ Unlimited & phone line rentals to residential customers.

TYPE: This project is for DESIGN only (no code)

Source Files: I need all source files, fonts, images to be provided in ZIP format.

Logo: Existing (attached)

-Corporate Colours-
Black & Red (Same as Logo)
Others colours are fine as long as it looks corporate and modern.

-Pages-
Need another page to display our pricing plan

(1)Homepage Design
(2)Page to display our plans (needs to be in tables)
Example: http://lnkbrev.example/QwTr8k

-Pricing Plan-
(1) $59.95 / Month (Metro / City Areas)
(2) $79.95 / Month (Outside City Areas / Rural Areas)
Detailed Pricing plans is in PDF attached
Updates

Target Market(s)

Both male & female, Young & Old

Industry/Entity Type

Residential

Requirements
Must have
• + Graphic banner on the home page that shows our ADSL2+ combo plan for ADSL2+ Unlimited & Phone Line Rental for only $59.95

+ A box to allow customers to login to their account (username & password + login button)

+ Clearly display contact number
+ Button to sign up
+ Button to check service availability something like https://checkin.pelwara.example/wizard/

+ Button for Live Chat
+ Navigation menu
+ Social media icons Facebook, Google +, Twitter
+ Minimal text on homepage
+ Corporate & Friendly
Nice to have
• + Effective use of icons with corporate colours
+ Effective use of stockphotos
(use of people in photos would be nice)

+ Effective use of graphics to navigate people through the site and inform customers of specials,etc.
Should not have
• + Cluttered
+ Don’t want long scrolling homepage
+ Don’t want too much text on homepage 500 words is the estimate max.

```html
<!DOCTYPE html>
<html lang="en">
<head>
<meta charset="utf-8">
<title>Vantrel – ADSL2+ &amp; Phone Line</title>
<link href="https://fonts.googleapis.com/css2?family=Arimo:wght@400;700&family=Oswald:wght@600;700&family=Roboto+Slab:wght@500;700&display=swap" rel="stylesheet">
<style>
  :root{
    --red:#e3342b;
    --red-dark:#a9151a;
    --charcoal:#2b2a2b;
    --ink:#1c1c1c;
    --grey-text:#555;
    --muted:#8a8a8a;
    --page-bg:#efefef;
    --white:#fff;
  }
  *{box-sizing:border-box;margin:0;padding:0}
  html,body{width:1170px;height:1200px;overflow:hidden}
  body{background:var(--page-bg);font-family:"Arimo",Arial,sans-serif;color:var(--ink);position:relative}
  .site{position:absolute;left:98px;top:46px;width:974px;height:1111px;background:var(--white);border-top:5px solid var(--red);box-shadow:0 0 8px rgba(0,0,0,.12)}
  .site > *{position:absolute}

  .brand{left:27px;top:30px;height:57px;display:flex;align-items:center;gap:10px}
  .brand-mark{width:54px;height:54px;border-radius:50%;background:var(--charcoal)}
  .brand-name{font-size:42px;font-weight:400;letter-spacing:2px;color:var(--ink)}
  .account-links{right:13px;top:14px;font-size:12px;color:var(--ink)}
  .account-links span{margin:0 6px}
  .call-us{right:13px;top:78px;font-size:24px;color:var(--ink)}
  .call-us strong{font-weight:400;color:var(--red)}

  .main-nav{left:0;top:120px;width:974px;height:45px;background:var(--charcoal);display:flex}
  .main-nav a{color:var(--white);text-decoration:none;font-size:14px;line-height:45px;padding:0 19px}
  .main-nav a.active{background:var(--red);padding:0 21px}

  .hero{left:12px;top:178px;width:674px;height:343px;overflow:hidden}
  .hero-photo{width:100%;height:100%;background:linear-gradient(100deg,#3a3f55 0%,#c9a896 28%,#ececec 48%,#f4f4f4 70%,#5a5a5a 88%,#e6e6e6 100%)}
  .hero-callout{position:absolute;left:324px;top:26px;width:350px;height:108px;background:var(--red);color:var(--white);padding:14px 14px}
  .hero-callout h1{font-size:30px;font-weight:700;line-height:1}
  .hero-callout p{font-size:17px;font-weight:700;line-height:20px;margin-top:12px}

  .availability{left:12px;top:535px;width:674px;height:173px;background:linear-gradient(100deg,#d8262a 0%,#c41c20 55%,#8e0d12 100%);color:var(--white)}
  .availability h2{position:absolute;left:16px;top:11px;font-size:26px;font-weight:400}
  .phone-field{position:absolute;left:19px;top:52px;width:518px;height:39px;background:var(--white);border-radius:3px;display:flex;align-items:center;padding-left:9px;gap:12px;color:#9a9a9a;font-size:18px}
  .btn-browse{position:absolute;left:545px;top:52px;width:107px;height:39px;border-radius:3px;background:linear-gradient(#fff,#dcdcdc);color:var(--red);font-weight:700;font-size:20px;text-align:center;line-height:39px}
  .availability .note{position:absolute;left:19px;top:98px;width:600px;font-size:14px;line-height:15px}
  .dont-call{position:absolute;left:19px;top:144px;font-size:14px;display:flex;align-items:center;gap:6px}
  .dont-call i{width:14px;height:14px;background:var(--white);border-radius:3px}

  .welcome{left:22px;top:752px;width:640px}
  .welcome h2{font-size:21px;font-weight:400;color:var(--red)}
  .welcome h2 span{color:var(--ink)}
  .welcome .lead{font-size:17px;font-weight:700;line-height:19px;margin-top:14px}
  .welcome p{font-size:15px;line-height:19px;color:var(--grey-text);margin-top:17px}
  .welcome p + p{margin-top:20px}

  .live-chat{left:701px;top:178px;width:261px;height:113px;background:linear-gradient(100deg,#b2151b 0%,#cf2228 60%,#e9e3e0 78%,#8a1115 100%);overflow:hidden}
  .live-chat .label{position:absolute;left:12px;top:28px;font-family:"Oswald",sans-serif;color:var(--white);line-height:.95;text-transform:uppercase}
  .live-chat .small{font-size:21px;font-weight:600;display:block}
  .live-chat .big{font-size:36px;font-weight:700;display:block}
  .live-chat .agent{position:absolute;right:0;top:0;width:72px;height:113px;background:linear-gradient(#f1ebe6,#c7a48d 60%,#9a1318)}

  .login-box{left:701px;top:305px;width:261px;height:216px;background:var(--charcoal)}
  .login-head{height:40px;background:var(--red);display:flex;align-items:center;gap:8px;padding-left:12px;color:var(--white);font-size:21px}
  .login-box .field{position:absolute;left:15px;width:229px;height:31px;background:var(--white);border-radius:3px}
  .login-box .f1{top:67px}.login-box .f2{top:107px}
  .forgot{position:absolute;left:15px;top:160px;font-size:13px;line-height:16px;color:#cfcfcf}
  .btn-login{position:absolute;left:166px;top:161px;width:78px;height:31px;background:var(--red);border-radius:3px;color:var(--white);font-size:19px;font-weight:700;text-align:center;line-height:31px}

  .promo{left:701px;top:535px;width:261px;height:294px;background:linear-gradient(160deg,#3a3a3a,#1f1f1f);text-align:center;font-family:"Roboto Slab",serif;color:var(--white);padding-top:18px}
  .promo .l1{font-size:33px;font-weight:500;line-height:34px}
  .promo .l2{font-size:33px;font-weight:500;line-height:34px;color:#b8b8b8}
  .promo .l3{font-size:23px;font-weight:700;line-height:24px;margin-top:2px}
  .promo .l4{font-size:23px;font-weight:500;line-height:24px}
  .promo .price{font-size:58px;font-weight:700;color:var(--red);line-height:62px}
  .btn-promo{position:absolute;left:67px;top:234px;width:129px;height:31px;background:linear-gradient(#fff,#cfcfcf);border-radius:3px;color:var(--ink);font-size:17px;font-weight:700;line-height:31px}

  .follow{left:701px;top:853px;width:261px;display:flex;justify-content:center;align-items:center;gap:6px;font-size:20px;color:var(--muted)}
  .follow .label{margin-right:6px}
  .social{width:28px;height:28px;background:#6b6b6b}

  .brand-small{left:736px;top:940px;display:flex;align-items:center;gap:6px}
  .brand-small .brand-mark{width:32px;height:32px}
  .brand-small .brand-name{font-size:25px;letter-spacing:1px}

  .site-footer{left:0;top:1011px;width:974px;height:95px;background:var(--charcoal);border-bottom:5px solid var(--red);text-align:center}
  .footer-nav{margin-top:24px;font-size:14px}
  .footer-nav a{color:#a8a8a8;text-decoration:none;margin:0 9px}
  .footer-nav a.active{color:var(--white)}
  .copyright{margin-top:10px;font-size:13.5px;color:#8f8f8f}
</style>
</head>
<body>
<div class="site">
  <div class="brand"><span class="brand-mark"></span><span class="brand-name">VANTREL</span></div>
  <div class="account-links">Sign up<span>|</span>Login</div>
  <div class="call-us">Call Us: <strong>000-000-0000</strong></div>

  <nav class="main-nav">
    <a class="active" href="#">HOME</a><a href="#">ABOUT US</a><a href="#">OUR PLANS</a><a href="#">CONTACT US</a>
  </nav>

  <section class="hero">
    <div class="hero-photo" role="img" aria-label="Photo of a smiling businessman beside an ADSL modem and router"></div>
    <div class="hero-callout">
      <h1>Sed lacinia vulputate</h1>
      <p>Nam quis ligula a nibh fermentum atis vitae nec neque. Etiam non felis</p>
    </div>
  </section>

  <section class="availability">
    <h2>Check service availability</h2>
    <div class="phone-field">
      <svg width="22" height="22" viewBox="0 0 24 24" aria-hidden="true"><path fill="#777" d="M6.6 10.8a15 15 0 0 0 6.6 6.6l2.2-2.2a1 1 0 0 1 1-.25 11.4 11.4 0 0 0 3.6.57 1 1 0 0 1 1 1V20a1 1 0 0 1-1 1A17 17 0 0 1 3 4a1 1 0 0 1 1-1h3.5a1 1 0 0 1 1 1c0 1.25.2 2.45.57 3.57a1 1 0 0 1-.25 1z"/></svg>
      Enter your phone number
    </div>
    <div class="btn-browse">Browse</div>
    <p class="note">By entering a number you agree that we may contact you to discuss the availability of services in your area.</p>
    <div class="dont-call"><i></i>Don't Call me</div>
  </section>

  <section class="welcome">
    <h2>WELCOME TO <span>VANTREL</span></h2>
    <p class="lead">Nam quis ligula a nibh fermentum venenatis vitae nec neque. Etiam non felis Quisque feugiat, lectus non feugiat consectetur,</p>
    <p>Aenean dapibus lorem laoreet ante pharetra ornare malesuada orci ornare. Ut volutpat ipsum ipsum, eget suscipit mauris. Sed sed nisl ac justo rutrum convallis. Fusce facilisis, nunc et viverra iaculis, arcu augue tempor ipsum,</p>
    <p>ut auctor sapien justo ac metus. Morbi adipiscing sodales condimentum. Nunc porta hendrerit turpis, nec pharetra enim interdum id.</p>
  </section>

  <aside class="live-chat">
    <div class="label"><span class="small">Click here for</span><span class="big">Live Chat</span></div>
    <div class="agent" role="img" aria-label="Photo of a support agent wearing a headset"></div>
  </aside>

  <aside class="login-box">
    <div class="login-head">
      <svg width="24" height="20" viewBox="0 0 24 20" aria-hidden="true"><circle cx="8" cy="6" r="4" fill="#fff"/><path d="M0 19c0-5 3.5-7 8-7s8 2 8 7z" fill="#fff"/><circle cx="17" cy="5" r="3.2" fill="#fff" opacity=".8"/><path d="M13 11.5c1-1 2.5-1.5 4-1.5 4 0 7 2 7 6h-6c0-2-2-3.7-5-4.5z" fill="#fff" opacity=".8"/></svg>
      User Login
    </div>
    <div class="field f1"></div>
    <div class="field f2"></div>
    <div class="forgot">• Forgot password?<br>• Forgot username?</div>
    <div class="btn-login">Login</div>
  </aside>

  <aside class="promo">
    <div class="l1">ADSL2+</div>
    <div class="l2">UNLIMITED</div>
    <div class="l3">&amp; PHONE LINE</div>
    <div class="l4">RENTAL</div>
    <div class="l4">FOR ONLY</div>
    <div class="price">$59.95</div>
    <div class="btn-promo">CLICK HERE</div>
  </aside>

  <div class="follow"><span class="label">Follow Us On</span><span class="social" aria-label="Social network 1"></span><span class="social" aria-label="Social network 2"></span><span class="social" aria-label="Social network 3"></span></div>

  <div class="brand-small"><span class="brand-mark"></span><span class="brand-name">VANTREL</span></div>

  <footer class="site-footer">
    <div class="footer-nav"><a class="active" href="#">Home</a><a href="#">About Us</a><a href="#">Our Plans</a><a href="#">Contact Us</a><a href="#">Terms &amp; Condition</a><a href="#">Privacy</a><a href="#">Login</a></div>
    <div class="copyright">Copyright © Vantrel 2013. All rights reserved.</div>
  </footer>
</div>
</body>
</html>
```